Business card for Drone Aerial

I need a business card designed keeping in mind I want to do post cards also with a similar design.
Both sides of the card would be cool.
I have a skylark 5 max and would like a picture of it on the front of the card. Similar to one I attached.
I really like the look of a drone in the air and the background pic a little blurry. I attached a few images as IDEAS.
Some special things I want to be on the card additional to the normal business card info:
"Aerial Photography" or "Low Altitude Aerial Photography"?
"ZQB# 90817263"

I like modern and creative. My Favorite color is blue and I like blue on white.
I do not have a business name and am not going to have one. When they read "Aerial Photography" and see the drone and image they will know what the card is for.

FYI, The attached pictures are just images from framewillow and just samples/ideas.

Target Market(s)

Real estate, construction, events

Industry/Entity Type

Business

Contact Information for Business Card

Also Definitely want to contain, my name, my number and email address.

Requirements
Must have
• "ZQB# 90817263"
• "Aerial Photography"

```html
<!DOCTYPE html>
<html lang="en">
<head>
<meta charset="utf-8">
<title>Aerial Photography – Business Card</title>
<link href="https://fonts.googleapis.com/css2?family=Open+Sans:wght@400;600;700&display=swap" rel="stylesheet">
<style>
  :root {
    --brand-blue: #1f64b8;
    --deep-blue: #1452a6;
    --sky-top: #2f74c8;
    --sky-mid: #4a8ad6;
    --sky-bottom: #7fb0e4;
    --drone-white: #f2f4f7;
    --drone-grey: #c9cfd8;
    --card-white: #f7f7f5;
    --ink-grey: #5a5f66;
    --stage: #e9e6e1;
  }
  * { box-sizing: border-box; margin: 0; padding: 0; }
  html, body {
    width: 1200px; height: 1023px; overflow: hidden;
    background: var(--stage);
    font-family: "Open Sans", Arial, sans-serif;
  }
  .canvas { position: relative; width: 1200px; height: 1023px; }

  .card {
    position: absolute; width: 600px; height: 340px;
    border-radius: 4px; overflow: hidden;
    box-shadow: 0 10px 28px rgba(0,0,0,.22);
  }

  /* Front */
  .card--front { left: 60px; top: 100px; background: var(--card-white); }
  .front__photo {
    height: 120px;
    background:
      radial-gradient(ellipse 90px 34px at 60% 30%, var(--drone-white), rgba(242,244,247,0) 75%),
      radial-gradient(ellipse 170px 58px at 62% 48%, rgba(201,207,216,.85), rgba(201,207,216,0) 72%),
      radial-gradient(ellipse 60px 30px at 80% 70%, rgba(230,234,240,.8), rgba(230,234,240,0) 75%),
      radial-gradient(ellipse 120px 50px at 15% 20%, rgba(255,255,255,.18), rgba(255,255,255,0) 70%),
      linear-gradient(180deg, var(--sky-top), var(--sky-mid) 55%, var(--sky-bottom));
  }
  .front__body { padding: 12px 36px 0 36px; }
  .brand { display: flex; align-items: center; gap: 14px; }
  .brand__circle { width: 56px; height: 56px; border-radius: 50%; background: var(--brand-blue); flex: none; }
  .brand__name {
    color: var(--brand-blue); font-weight: 700; font-size: 28px; letter-spacing: .5px;
  }
  .contact { margin: 4px 0 0 70px; color: var(--ink-grey); font-size: 13px; line-height: 17px; }
  .contact__name { color: var(--brand-blue); font-weight: 700; font-size: 20px; line-height: 26px; letter-spacing: .5px; }
  .contact__role { font-size: 12px; margin-bottom: 3px; }
  .contact__line { display: flex; align-items: center; gap: 6px; }
  .contact__line--indent { padding-left: 18px; }
  .contact__icon { width: 12px; height: 12px; fill: var(--ink-grey); flex: none; }
  .contact__licence { color: var(--brand-blue); font-weight: 600; }

  /* Back */
  .card--back {
    left: 560px; top: 580px;
    background: linear-gradient(160deg, #2a72c6, var(--deep-blue));
    display: flex; align-items: center; justify-content: center; gap: 22px;
  }
  .back__circle { width: 120px; height: 120px; border-radius: 50%; background: #fff; flex: none; }
  .back__name { color: #fff; font-weight: 600; font-size: 30px; letter-spacing: 1px; }
</style>
</head>
<body>
<main class="canvas">

  <section class="card card--front">
    <div class="front__photo" role="img" aria-label="Photo of a white quadcopter camera drone hovering close up against a softly blurred blue sky"></div>
    <div class="front__body">
      <div class="brand">
        <span class="brand__circle"></span>
        <span class="brand__name">AERIAL PHOTOGRAPHY</span>
      </div>
      <div class="contact">
        <div class="contact__name">MAREN HOLLOWAY</div>
        <div class="contact__role">Director</div>
        <div class="contact__line">
          <svg class="contact__icon" viewBox="0 0 12 12"><path d="M2.2 0.8 4 0.5 5 3 3.9 4.1c.6 1.5 1.7 2.6 3.2 3.2L8.2 6.2 10.7 7.2 10.4 9c-.1.6-.6 1-1.2 1C4.7 9.8 1.6 6.7 1.4 2c0-.6.4-1.1.8-1.2z"/></svg>
          <span>0400 555 274</span>
        </div>
        <div class="contact__line">
          <svg class="contact__icon" viewBox="0 0 12 12"><path d="M0.5 2h11v8h-11z" fill="none" stroke="#5a5f66" stroke-width="1.2"/><path d="M0.5 2 6 6.5 11.5 2" fill="none" stroke="#5a5f66" stroke-width="1.2"/></svg>
          <span>maren@skyframe-studio.com.au</span>
        </div>
        <div class="contact__line contact__line--indent">Consulting Rooms</div>
        <div class="contact__line contact__line--indent">42 Larkspur Lane, Eastbrook VIC 3999</div>
        <div class="contact__line contact__line--indent contact__licence">ZQB# 90817263</div>
      </div>
    </div>
  </section>

  <section class="card card--back">
    <span class="back__circle"></span>
    <span class="back__name">AERIAL PHOTOGRAPHY</span>
  </section>

</main>
</body>
</html>
```